New Webpage for High Class Expert Witness Services Company

We are looking for a minimalist design for a webpage that just has our logo and an entry form offer to connect with one of our Liaisons.
The entry form should just ask for Name, Email, Contact Info and Description of Project.

Company Name is: The Marlow Crest Advisory Services

Number of Pages Required

1 page

```html
<!DOCTYPE html>
<html lang="en">
<head>
<meta charset="UTF-8">
<title>Marlow Crest Advisory Services — Connect With a Liaison</title>
<link href="https://fonts.googleapis.com/css2?family=Outfit:wght@300;400;500;600&display=swap" rel="stylesheet">
<style>
  :root {
    --bg: #0a0a0b;
    --panel: #0d0d0e;
    --card: #131314;
    --card-border: #242426;
    --line: #3a3a3c;
    --label: #8a8a8c;
    --placeholder: #5c5c5f;
    --heading: #7c7c80;
    --white: #f2f2f2;
    --muted: #3c3c3f;
    --button-a: #9c9ca2;
    --button-b: #c6c6cc;
    --button-text: #0c0c0c;
    --emblem-top: #4a4a4c;
    --emblem-bottom: #262628;
  }
  * { box-sizing: border-box; margin: 0; padding: 0; }
  html, body {
    width: 1200px; height: 639px; overflow: hidden;
    background: var(--bg);
    font-family: "Outfit", sans-serif;
  }
  .page { position: relative; width: 1200px; height: 639px; }

  .emblem {
    position: absolute; left: 13px; top: 313px; width: 250px; height: 297px;
    background: linear-gradient(180deg, var(--emblem-top), var(--emblem-bottom));
    opacity: .75;
    clip-path: polygon(0 0, 100% 0, 100% 100%, 30% 100%, 0 70%);
  }

  .brand-panel {
    position: absolute; left: 627px; top: 80px; width: 278px; height: 130px;
    background: var(--panel);
  }
  .brand {
    position: absolute; left: 686px; top: 140px;
    display: flex; align-items: center; gap: 8px;
  }
  .brand-mark { width: 12px; height: 12px; background: var(--white); }
  .brand-name {
    color: var(--white); font-weight: 500; font-size: 12px; letter-spacing: .08em;
    text-transform: uppercase; white-space: nowrap;
  }

  .section-title {
    position: absolute; left: 627px; top: 227px;
    color: var(--heading); font-weight: 400; font-size: 10.5px; letter-spacing: .17em;
  }

  .inquiry-card {
    position: absolute; left: 627px; top: 264px; width: 346px; height: 273px;
    background: var(--card); border: 1px solid var(--card-border); border-radius: 12px;
  }
  .field { position: absolute; border-bottom: 1px solid var(--line); }
  .field label {
    display: block; color: var(--label); font-size: 7px; font-weight: 600; letter-spacing: .14em;
  }
  .field span {
    display: block; color: var(--placeholder); font-size: 10px; font-weight: 300;
    letter-spacing: .05em; margin-top: 12px;
  }
  .field-name { left: 27px; top: 25px; width: 140px; height: 44px; }
  .field-email { left: 179px; top: 25px; width: 140px; height: 44px; }
  .field-contact { left: 27px; top: 85px; width: 292px; height: 43px; }
  .field-desc { left: 27px; top: 144px; width: 292px; height: 47px; }
  .field-desc span { text-transform: none; letter-spacing: .02em; margin-top: 14px; }

  .submit-button {
    position: absolute; left: 27px; top: 213px; width: 152px; height: 35px;
    border-radius: 18px;
    background: linear-gradient(90deg, var(--button-a), var(--button-b));
    box-shadow: 0 0 14px rgba(200,200,210,.12);
    display: flex; align-items: center; justify-content: center; gap: 8px;
    color: var(--button-text); font-size: 8px; font-weight: 600; letter-spacing: .14em;
  }

  .assurances {
    position: absolute; left: 627px; top: 552px;
    display: flex; gap: 14px; align-items: center;
    color: var(--muted); font-size: 6px; letter-spacing: .1em;
  }
  .assurances i { width: 2px; height: 2px; border-radius: 50%; background: var(--muted); }

  .footer-left, .footer-right {
    position: absolute; top: 621px; color: #2c2c2e; font-size: 6px; letter-spacing: .1em;
  }
  .footer-left { left: 21px; }
  .footer-right { right: 30px; }
  .chat-dot {
    position: absolute; left: 1162px; top: 602px; width: 25px; height: 25px;
    border-radius: 50%; background: #050505; border: 1px solid #3a3a3c;
  }
</style>
</head>
<body>
<main class="page">
  <div class="emblem" role="img" aria-label="Large faint brand emblem decoration"></div>

  <div class="brand-panel"></div>
  <div class="brand">
    <span class="brand-mark"></span>
    <span class="brand-name">Marlow Crest Advisory Services</span>
  </div>

  <h1 class="section-title">CONNECT WITH ONE OF OUR LIAISONS</h1>

  <form class="inquiry-card">
    <div class="field field-name"><label>FULL NAME</label><span>JOHN SMITH</span></div>
    <div class="field field-email"><label>EMAIL</label><span>EXAMPLE@MAIL.COM</span></div>
    <div class="field field-contact"><label>CONTACT INFO</label><span>PHONE OR PREFERRED METHOD</span></div>
    <div class="field field-desc"><label>DESCRIPTION OF PROJECT</label><span>Briefly describe your project or inquiry...</span></div>
    <div class="submit-button">SUBMIT INQUIRY
      <svg width="10" height="6" viewBox="0 0 10 6"><path d="M0 3h9M6.5 .5L9 3 6.5 5.5" stroke="#0c0c0c" stroke-width="1" fill="none"/></svg>
    </div>
  </form>

  <div class="assurances">
    <span>CONFIDENTIAL</span><i></i><span>VETTED EXPERTS</span><i></i><span>24/7 RESPONSE</span>
  </div>

  <p class="footer-left">© 2026 THE MARLOW CREST ADVISORY SERVICES</p>
  <p class="footer-right">CONFIDENTIAL &amp; SECURE</p>
  <div class="chat-dot"></div>
</main>
</body>
</html>
```